Visualisation Software brochure

i need a sales brochure for a new visualisation software company called Lumora Scene Studio.
The software has been specifically designed for manufacturers, distributers and retailers in the design / décor / furnishing / building industries. It allows customers can then import unlimited numbers of digital photos of rooms from their own home or take advantage of a library of pre-made photos, and then render different products from your catalogue into that photo to see what the finished look will be.
i have attached:
1) a mock up of the home page of the website
2) example of brochure wording that i have put together (although i am a little unsure about what other words i can add - so any suggestions here would be good)
3) i have attached some examples of other brochures that i like and would like similar designs
I am after a classy brochure used by a large corporate technology company that is given to executives and gives an impression of quality, trustworthiness and innovation.
• the colour blue as per the colours on my website mock up provided in the design brief
• I like simple, smart, clean and uncluttered design
• I like simple, clean and uncluttered design
• I like pictures that fit in with my technology (whether that be home and interior design, mixing virtual world and real world, visualising an idea) rather than basic stock of corporate people
Updates
Target Market(s)
marketing professionals
Industry/Entity Type
Software
Font styles to use
Look and feel
Each slider illustrates characteristics of the customer's brand and the style your logo design should communicate.

```html
<!DOCTYPE html>
<html lang="en">
<head>
<meta charset="utf-8">
<title>Sales process – 6 steps to success</title>
<link rel="stylesheet" href="https://fonts.googleapis.com/css2?family=Roboto+Condensed:wght@300;400&display=swap">
<style>
  :root {
    --photo-white: #f7f8fb;
    --photo-pale: #dfe5ee;
    --photo-light: #c3cedf;
    --photo-mid: #8fa1bd;
    --photo-deep: #4f6489;
    --photo-ink: #1f2f4f;
    --band: rgba(232, 234, 239, 0.80);
    --text: #2e2e2e;
    --heading: #242424;
  }
  * { margin: 0; padding: 0; box-sizing: border-box; }
  html, body {
    width: 848px;
    height: 1200px;
    overflow: hidden;
    background: #ffffff;
  }
  .page {
    position: relative;
    width: 848px;
    height: 1200px;
    overflow: hidden;
    font-family: "Roboto Condensed", "Arial Narrow", sans-serif;
  }
  .page__photo {
    position: absolute;
    inset: 0;
    background:
      /* upper right: screen and keyboard tones */
      radial-gradient(ellipse 150px 230px at 790px 90px, rgba(79, 100, 137, 0.75), transparent 75%),
      radial-gradient(ellipse 330px 120px at 600px 290px, rgba(95, 117, 155, 0.55), transparent 75%),
      radial-gradient(ellipse 260px 160px at 560px 470px, rgba(143, 161, 189, 0.5), transparent 75%),
      /* upper left: rolled plans */
      radial-gradient(ellipse 110px 150px at 70px 260px, rgba(79, 100, 137, 0.6), transparent 75%),
      radial-gradient(ellipse 260px 110px at 290px 250px, rgba(195, 206, 223, 0.75), transparent 75%),
      /* lower: pen lying diagonally over drawings */
      linear-gradient(160deg, transparent 68%, rgba(31, 47, 79, 0.0) 70%, rgba(31, 47, 79, 0.55) 74%, rgba(31, 47, 79, 0.2) 77%, transparent 80%),
      radial-gradient(ellipse 420px 140px at 380px 1000px, rgba(79, 100, 137, 0.35), transparent 75%),
      radial-gradient(ellipse 300px 160px at 760px 1130px, rgba(143, 161, 189, 0.45), transparent 75%),
      linear-gradient(180deg,
        var(--photo-white) 0%,
        var(--photo-pale) 12%,
        var(--photo-light) 28%,
        var(--photo-pale) 45%,
        var(--photo-light) 62%,
        var(--photo-pale) 74%,
        var(--photo-light) 88%,
        var(--photo-mid) 100%);
  }
  .process-band {
    position: absolute;
    left: 0;
    top: 352px;
    width: 848px;
    height: 496px;
    background: var(--band);
  }
  .process {
    position: absolute;
    left: 317px;
    top: 385px;
    width: 503px;
    color: var(--text);
  }
  .process__title {
    font-weight: 400;
    font-size: 23.3px;
    line-height: 30px;
    color: var(--heading);
    margin-bottom: 9px;
  }
  .process__steps {
    list-style: none;
    counter-reset: step;
  }
  .process__step {
    counter-increment: step;
    position: relative;
    padding-left: 23px;
    font-size: 16.3px;
    font-weight: 400;
    line-height: 22px;
    text-align: justify;
    margin-bottom: 18.5px;
  }
  .process__step::before {
    content: counter(step) ".";
    position: absolute;
    left: 0;
    top: 0;
  }
  .process__closing {
    font-size: 16.3px;
    line-height: 22px;
    margin-top: 1px;
  }
</style>
</head>
<body>
  <main class="page">
    <div class="page__photo" role="img" aria-label="Blue-toned photograph of a laptop keyboard, rolled architectural plans and a ballpoint pen lying on technical drawings"></div>

    <div class="process-band"></div>

    <section class="process">
      <h1 class="process__title">Sales process - 6 steps to success</h1>
      <ol class="process__steps">
        <li class="process__step">Leverage the internet and the power of word-of-mouth</li>
        <li class="process__step">Increase interest / desire via the website by seeing how virtualised product placement works – so that’s how my house or room will look if I buy those products</li>
        <li class="process__step">Combine the virtual and real worlds during an in-store or onsite consultation – virtual walk through your products combined with physical samples</li>
        <li class="process__step">Sales consultants qualify customer requirements</li>
        <li class="process__step">Trial close by sales consultant – what is required for the customer to purchase</li>
        <li class="process__step">Full sales opportunity close and determine steps to purchase / register</li>
      </ol>
      <p class="process__closing">It all leads to the register</p>
    </section>
  </main>
</body>
</html>
```